innovative design Cafe Menu

looking for an innovative design for a food menu for a coffee shop and take away restaurant.

Target Market(s)

Canada

Requirements
Must have
• innovative design and easy to navigate and reading

```html
<!DOCTYPE html>
<html lang="en">
<head>
<meta charset="utf-8">
<title>Mira's Cafe Menu</title>
<link href="https://fonts.googleapis.com/css2?family=Source+Serif+4:wght@400;600;700&family=Roboto:wght@400;500;700&display=swap" rel="stylesheet">
<style>
:root{
  --green-dark:#0d5a25;
  --green-bar:#4fa34a;
  --green-item:#4f9f45;
  --green-light:#5aae4c;
  --maroon:#7a1f2c;
  --orange:#f5a623;
  --ink:#222;
  --white:#fff;
}
*{margin:0;padding:0;box-sizing:border-box}
html,body{width:1200px;height:849px;overflow:hidden;background:var(--white)}
.menu{position:relative;width:1200px;height:849px;overflow:hidden;font-family:"Source Serif 4",serif;color:var(--ink)}
.panel{position:absolute;top:0;height:849px}
.panel-left{left:0;width:400px;background:var(--white)}
.panel-mid{left:400px;width:400px;background:var(--white)}
.panel-mid .green-field{position:absolute;left:0;top:0;width:400px;height:613px;background:var(--green-dark)}
.panel-right{left:800px;width:400px;background:var(--white)}
.photo{position:absolute}
.photo-burger{left:115px;top:38px;width:160px;height:120px;border-radius:50% 50% 40% 40%;background:radial-gradient(circle at 50% 45%,#c7802f,#7a4a22 55%,#e8b467 80%,rgba(255,255,255,0) 82%)}
.photo-dessert{left:0;top:630px;width:400px;height:219px}
.photo-kid{left:0;top:613px;width:400px;height:236px;background:linear-gradient(120deg,#d7dde6 0%,#eef1f4 45%,#c9a57a 70%,#e9eef0 100%)}
.section-bar{position:absolute;left:22px;width:356px;height:23px;background:var(--green-bar);color:var(--white);font-weight:700;font-size:13.5px;line-height:23px;padding-left:8px}
.item{position:absolute;left:30px;width:348px}
.item-row{display:flex;align-items:baseline;font-size:14px}
.item-name{color:var(--green-item);font-weight:600;white-space:nowrap}
.leader{flex:1;border-bottom:1px dotted #555;margin:0 4px;transform:translateY(-3px)}
.item-price{white-space:nowrap;color:var(--ink)}
.item-desc{font-size:11.6px;line-height:16.2px;margin-top:1px}
.kids .section-bar{left:19px;width:355px}
.kids .item{left:26px;width:348px;color:var(--white)}
.kids .item-name{color:var(--green-light)}
.kids .item-price,.kids .leader{color:var(--white);border-color:#cfe3cf}
.brand{position:absolute;left:0;width:400px;top:448px;text-align:center;display:flex;justify-content:center;align-items:center;gap:10px}
.brand-mark{width:34px;height:34px;border-radius:50%;background:var(--green-item)}
.brand-name{font-family:"Source Serif 4",serif;font-weight:700;font-size:44px;color:var(--maroon)}
.info{position:absolute;left:0;width:400px;text-align:center;font-family:Roboto,sans-serif}
.site{top:573px;color:var(--green-item);font-weight:700;font-size:15px}
.address{top:661px;color:var(--maroon);font-size:14px}
.rule{position:absolute;left:88px;top:687px;width:222px;border-top:1px dotted var(--maroon)}
.hours-label{top:692px;color:var(--maroon);font-size:14px;font-weight:400}
.service{top:715px;color:var(--green-dark);font-weight:700;font-size:14px}
.hours{top:737px;color:var(--maroon);font-size:14px;line-height:20.5px;font-weight:500}
.contact{position:absolute;left:38px;top:787px;width:323px;height:62px;background:var(--green-dark);border-radius:18px 18px 0 0;color:var(--white);font-family:Roboto,sans-serif;font-size:12.5px}
.contact p{position:absolute;left:17px}
.contact .phone{top:14px}
.contact .email{top:34px}
.contact b{font-weight:500}
.contact .tag{position:absolute;right:13px;top:34px;font-weight:500}
.social{position:absolute;right:20px;top:12px;display:flex;gap:12px}
.social span{width:14px;height:14px;border-radius:50%;background:var(--white)}
</style>
</head>
<body>
<div class="menu">

  <section class="panel panel-left">
    <div class="photo photo-burger" role="img" aria-label="Photo of a cheeseburger with lettuce and tomato"></div>

    <div class="section-bar" style="top:167px">Burgers</div>
    <div class="item" style="top:197px">
      <div class="item-row"><span class="item-name">Rocco’s Burger</span><span class="leader"></span><span class="item-price">$ 7.59</span></div>
      <p class="item-desc">Fresh ground beef patty we have in the house mix<br>with our special seasonal top with melted Swiss Cheese<br>laying over black pepper and mushroom sauce</p>
    </div>
    <div class="item" style="top:271px">
      <div class="item-row"><span class="item-name">Melty Stack</span><span class="leader"></span><span class="item-price">$ 6.99</span></div>
      <p class="item-desc">Fresh ground beef patty we have in the house mix<br>with our special seasonal top with melted Swiss Cheese<br>laying over Mayo, pickle, tomato and lettuce on burger bun</p>
    </div>

    <div class="section-bar" style="top:350px">Hot Beverages</div>
    <div class="item" style="top:380px">
      <div class="item-row"><span class="item-name">Espresso</span><span class="leader"></span><span class="item-price">$ 2.50</span></div>
      <p class="item-desc">Roastline espresso</p>
    </div>
    <div class="item" style="top:421px">
      <div class="item-row"><span class="item-name">Cappuccino</span><span class="leader"></span><span class="item-price">$ 3.00</span></div>
    </div>
    <div class="item" style="top:447px">
      <div class="item-row"><span class="item-name">Vanilla Latte</span><span class="leader"></span><span class="item-price">$ 3.15</span></div>
      <p class="item-desc">Roastline Cafe latte vanilla flavour</p>
    </div>
    <div class="item" style="top:488px">
      <div class="item-row"><span class="item-name">Caramell latte</span><span class="leader"></span><span class="item-price">$ 3.15</span></div>
      <p class="item-desc">Carmel flavour Roastline Coffee latte</p>
    </div>

    <div class="section-bar" style="top:536px">Dessert</div>
    <div class="item" style="top:566px">
      <div class="item-row"><span class="item-name">Cheesecake</span><span class="leader"></span><span class="item-price">$ 4.00</span></div>
      <p class="item-desc">New York style cheesecake with<br>different topic (Caramel/Strawberry)</p>
    </div>
    <div class="item" style="top:624px">
      <div class="item-row"><span class="item-name">Crumble Cheesecake</span><span class="leader"></span><span class="item-price">$ 4.00</span></div>
    </div>

    <svg class="photo photo-dessert" viewBox="0 0 400 219" role="img" aria-label="Photo of cream-topped cookie cheesecakes on a plate">
      <defs>
        <linearGradient id="dessertTone" x1="0" y1="0" x2="1" y2="1">
          <stop offset="0" stop-color="#fdf6ec"/>
          <stop offset="0.5" stop-color="#e9c9a3"/>
          <stop offset="1" stop-color="#c98f7e"/>
        </linearGradient>
      </defs>
      <rect x="60" y="20" width="340" height="199" fill="url(#dessertTone)"/>
      <path d="M0,50 C40,55 60,90 80,140 C100,190 150,210 260,219 L0,219 Z" fill="var(--green-dark)"/>
      <path d="M0,70 C40,80 70,130 110,170 C150,205 220,210 310,219" fill="none" stroke="var(--white)" stroke-width="1.5"/>
      <path d="M0,110 C30,120 60,160 90,185 C120,210 170,215 230,219" fill="none" stroke="var(--orange)" stroke-width="2"/>
    </svg>
  </section>

  <section class="panel panel-mid">
    <div class="green-field"></div>
    <div class="kids">
      <div class="section-bar" style="top:320px">Kids Menu</div>
      <div class="item" style="top:350px">
        <div class="item-row"><span class="item-name">Chicken Tender</span><span class="leader"></span><span class="item-price">$ 5.99</span></div>
        <p class="item-desc">Tender juicy real chicken breast strips marinated<br>overnight breaded then fried topped served with french fries.</p>
      </div>
      <div class="item" style="top:408px">
        <div class="item-row"><span class="item-name">Cheese Burger</span><span class="leader"></span><span class="item-price">$ 5.99</span></div>
        <p class="item-desc">Fresh ground beed patty made n the house mix with<br>our special seasonal top with melted Swiss or Cheddar<br>cheese serves french fries.</p>
      </div>
      <div class="item" style="top:481px">
        <div class="item-row"><span class="item-name">Fish Fillet Sandwich</span><span class="leader"></span><span class="item-price">$ 5.99</span></div>
        <p class="item-desc">Breadedfried Haddock Chemical free fillet marinated<br>overnight laid over Tartar Sauce and lettuce on a bun servos.</p>
      </div>
      <div class="item" style="top:539px">
        <div class="item-row"><span class="item-name">Kofta Wrap</span><span class="leader"></span><span class="item-price">$ 5.99</span></div>
        <p class="item-desc">Barbeque ground beef our special seasoning serve<br>was the Tahini sauce pickle, lettuce and tomato served<br>with french fries.</p>
      </div>
    </div>
    <div class="photo photo-kid" role="img" aria-label="Photo of a smiling child beside a plated burger"></div>
  </section>

  <section class="panel panel-right">
    <div class="brand"><span class="brand-mark"></span><span class="brand-name">Mira’s Cafe</span></div>
    <p class="info site">www.miracafe.ca</p>
    <p class="info address">24 Birchwood Ave. Markham L3R 2K8</p>
    <div class="rule"></div>
    <p class="info hours-label">Opening hours :</p>
    <p class="info service">Dine In or Take Away</p>
    <p class="info hours">Monday - Friday &nbsp;|&nbsp; 11 AM – 8 PM<br>Saturday &amp; Sunday &nbsp;|&nbsp; 9 AM - 7 PM</p>
    <div class="contact">
      <p class="phone">Ph: <b>905-555-0142</b></p>
      <p class="email">E-Mail: <b>hello@miracafe.ca</b></p>
      <div class="social"><span></span><span></span><span></span></div>
      <span class="tag">#mirascafe.ca</span>
    </div>
  </section>

  <svg style="position:absolute;left:400px;top:0" width="800" height="430" viewBox="0 0 800 430" role="img" aria-label="Photo of falafel wraps on a wooden board with a sandwich shown in a round frame">
    <defs>
      <linearGradient id="wrapTone" x1="0" y1="0" x2="1" y2="1">
        <stop offset="0" stop-color="#2b2a38"/>
        <stop offset="0.55" stop-color="#3a3442"/>
        <stop offset="0.75" stop-color="#c9a66e"/>
        <stop offset="1" stop-color="#6b4a2f"/>
      </linearGradient>
      <radialGradient id="subTone" cx="0.5" cy="0.5" r="0.6">
        <stop offset="0" stop-color="#c98a4d"/>
        <stop offset="0.6" stop-color="#e6c79c"/>
        <stop offset="1" stop-color="#c8302e"/>
      </radialGradient>
    </defs>
    <path d="M98,0 C140,60 170,85 190,104 C232,140 238,220 256,252 C292,300 340,312 398,312 C500,312 560,320 620,338 C700,362 760,402 800,420 L800,0 Z" fill="url(#wrapTone)"/>
    <path d="M416,0 C440,40 470,62 510,68 C580,78 640,80 700,110 C740,130 770,148 800,156 L800,0 Z" fill="var(--green-dark)"/>
    <path d="M420,0 C445,46 480,70 530,76 C600,84 660,92 710,122 C745,142 775,156 800,162" fill="none" stroke="var(--orange)" stroke-width="2.5"/>
    <path d="M210,0 C260,60 330,100 420,110 C560,120 680,150 800,210" fill="none" stroke="var(--white)" stroke-width="1.5"/>
    <path d="M255,250 C300,290 380,296 470,300 C600,306 720,340 800,392" fill="none" stroke="var(--white)" stroke-width="1.5"/>
    <path d="M110,0 C140,40 160,70 165,95" fill="none" stroke="var(--white)" stroke-width="1"/>
    <circle cx="101" cy="135" r="53" fill="var(--green-light)"/>
    <circle cx="182" cy="180" r="86" fill="#d9d9d9"/>
    <circle cx="182" cy="180" r="79" fill="url(#subTone)"/>
    <circle cx="245" cy="240" r="16" fill="var(--white)"/>
    <circle cx="233" cy="271" r="8" fill="var(--green-light)"/>
  </svg>

</div>
</body>
</html>
```